Personal and Group Fitness Instructor Needs a Logo Design and Word Press page set up

I need a logo design and wordpress design for a personal and group training fitness instructor in Burlington, VT. I will be using videos on my page as well blog posts to write about different topics. My product is just creating content for people to view workouts, nutrition mental wellness, spirituality, and health topics. My goal is to use this website and other social media in the future to do remote personal and group training and create a community of people seeking self and world improvement. I would like the design to incorporate green trees or plants, some gold and maybe work in the tree/root design as well as a fitness component (barbell, dumbbell, or kettlebell) Vermont (where I am based) is known for its green mountains so I could like to incorporate something like that in there. Perhaps some sunset type colors would be great too but it could be too much going on. The design should communicate simplicity, strength, and spiritual growth. I would like to have a page with easy tabs to navigate, the tabs are a work in progress but the topics I'd like to have tabs for at this point would be : workouts, book reviews, blog, coaching, about. The blog is currently a work in progress.

Target Market(s)

anyone using the internet looking for ways to improve health, nutrition, mental wellness, spirituality, inspiration.

Industry/Entity Type

Health And Wellness

Logo Text

copper lantern

Font styles to use
Sans Serif

Requirements
Must have
• green, trees/plants,and some fitness (barbell, dumbbell, kettlebell) aspect as well as a spirituality aspect (mandala like art) to the logo design & website.
Nice to have
• It would be cool to see some type of sunrise or sunset aspect with a variety of colors going on in the background, if we could sneak in some mountain/water aspect that could be very nice. Almost a spiritual/jungle like feel with a fitness aspect :) I really like the blending of several ideas into one logo, like the fitness aspect blending into the jungle/ plant/ mandala/ type of logo.

```html
<!DOCTYPE html>
<html lang="en">
<head>
<meta charset="utf-8">
<title>Copper Lantern — Fitness &amp; Wellness</title>
<link rel="stylesheet" href="https://fonts.googleapis.com/css2?family=Open+Sans:wght@400;600;700&display=swap">
<style>
  :root{
    --green:#2f8f2f;
    --green-band:#3f8b1d;
    --gold:#f1a90d;
    --ink:#333;
    --muted:#666;
    --light:#ececec;
    --white:#fff;
    --footer:#262626;
    --footer-bottom:#222;
    --footer-text:#8a8a8a;
  }
  *{box-sizing:border-box;margin:0;padding:0}
  html,body{width:1200px;height:2812px;overflow:hidden;background:var(--white)}
  body{font-family:"Open Sans",Arial,sans-serif;color:var(--ink);position:relative}
  .abs{position:absolute}

  /* Header */
  .site-header{left:0;top:0;width:1200px;height:137px;background:var(--white)}
  .brand{left:131px;top:38px;display:flex;align-items:center;gap:12px}
  .brand-mark{width:34px;height:34px;border-radius:50%;background:var(--ink)}
  .brand-name{font-size:24px;font-weight:700;color:var(--ink);line-height:1.1;width:110px}
  .search{left:844px;top:38px;width:221px;height:39px;border:1px solid #ccc;display:flex;align-items:center;padding:0 14px;font-size:12px;color:#999;justify-content:space-between}
  .main-nav{right:135px;top:106px;display:flex;gap:30px;font-size:12.5px;text-transform:uppercase;color:#444}
  .main-nav .current{color:var(--green)}

  /* Hero */
  .hero{left:0;top:137px;width:1200px;height:478px;background:linear-gradient(180deg,#3a3f4a 0%,#b5652a 28%,#e9a33f 40%,#6b4a2c 52%,#2c3a22 70%,#38423a 85%,#2a2e22 100%)}
  .hero-arrow{top:232px;width:16px;height:16px}
  .hero-caption{left:131px;top:337px;width:934px;height:122px;background:rgba(20,20,20,.72);text-align:center;color:var(--white);padding-top:24px}
  .hero-caption h2{font-size:16px;font-weight:600;text-transform:uppercase;letter-spacing:.3px}
  .hero-caption .date{font-size:10.5px;margin-top:8px}
  .hero-caption p{font-size:10.5px;color:#ccc;margin:8px auto 0;width:840px;line-height:1.5}

  /* Welcome */
  .welcome{left:0;top:615px;width:1200px;height:615px;background:var(--light)}
  .welcome-media{left:0;top:0;width:600px;height:615px;background:linear-gradient(135deg,#5b5e5f 0%,#3b3d3e 45%,#1f2021 100%)}
  .play{left:272px;top:278px;width:56px;height:56px}
  .welcome h1{left:639px;top:68px;font-size:40px;font-weight:700;color:var(--green);letter-spacing:.5px}
  .welcome p{left:639px;top:138px;width:426px;font-size:11.5px;line-height:20.6px;color:#555}
  .btn-light{left:639px;top:353px;width:88px;height:33px;background:var(--white);font-size:11.5px;color:#555;display:flex;align-items:center;justify-content:center}
  .welcome-art{left:896px;top:323px;width:282px;height:282px;background:radial-gradient(circle,#dcdcdc 0%,#e8e8e8 55%,var(--light) 72%)}

  /* Featured posts */
  .featured{left:0;top:1230px;width:1200px;height:613px;background:linear-gradient(180deg,#1e211a 0%,#2b2e22 50%,#1a1c17 100%)}
  .section-title{width:1200px;text-align:center;font-size:28px;font-weight:700;color:var(--gold);letter-spacing:.5px}
  .post-card{top:107px;width:298px;height:382px;background:#ececec}
  .post-media{width:298px;height:191px}
  .post-date{left:0;top:166px;height:28px;padding:0 16px 0 18px;background:var(--gold);font-size:11px;font-weight:700;color:#222;display:flex;align-items:center}
  .post-body{left:17px;top:211px;width:266px;display:flex;flex-direction:column;gap:9px}
  .post-body h3{font-size:14px;font-weight:400;line-height:19px;color:#222;letter-spacing:-.2px}
  .post-body p{font-size:9.5px;line-height:15px;color:#777}
  .post-more{left:17px;bottom:20px;font-size:12.5px;color:var(--green);font-weight:600}
  .btn-outline{width:80px;height:35px;border:1px solid #ddd;color:var(--white);font-size:10.5px;font-weight:600;display:flex;align-items:center;justify-content:center;left:559px}

  /* Workouts */
  .workouts{left:0;top:1843px;width:1200px;height:553px;background:linear-gradient(180deg,#2a2620 0%,#3b342a 40%,#2c281f 75%,#221f19 100%)}
  .workout{top:131px;width:161px}
  .workout-media{width:161px;height:160px}
  .workout h3{margin-top:22px;font-size:18px;font-weight:700;line-height:22px;color:var(--white);text-transform:uppercase}
  .workout p{margin-top:4px;font-size:10.5px;line-height:16px;color:#ddd}

  /* Newsletter */
  .newsletter{left:0;top:2396px;width:1200px;height:96px;background:var(--green-band)}
  .newsletter-title{left:131px;top:27px;display:flex;align-items:center;gap:10px;color:var(--white);font-size:30px}
  .field{top:29px;width:219px;height:38px;background:var(--white);font-size:11.5px;color:#555;display:flex;align-items:center;padding-left:14px}
  .btn-dark{left:967px;top:29px;width:98px;height:38px;background:#1b1b1b;color:var(--white);font-size:11.5px;font-weight:700;display:flex;align-items:center;justify-content:center}

  /* Footer */
  .site-footer{left:0;top:2492px;width:1200px;height:260px;background:var(--footer)}
  .footer-col h4{font-size:12.5px;font-weight:400;color:var(--white)}
  .footer-links{left:131px;top:34px;list-style:none}
  .footer-links li{font-size:12.5px;color:var(--white);height:32px}
  .blog-col{left:272px;top:34px;width:290px}
  .blog-col p{font-size:10px;line-height:15px;color:var(--footer-text);margin-top:24px}
  .blog-col p + p{margin-top:27px}
  .coach-col{left:616px;top:34px}
  .coach-col ul{list-style:none;margin-top:16px}
  .coach-col li{font-size:10px;color:var(--footer-text);height:26px}
  .about-col{left:787px;top:34px;width:190px}
  .about-col p{font-size:10px;line-height:15.5px;color:var(--footer-text);margin-top:16px}
  .social{left:1033px;width:34px;height:34px;border-radius:2px}
  .copyright{left:0;top:2752px;width:1200px;height:60px;background:var(--footer-bottom);border-top:1px solid #333;text-align:center;font-size:10.5px;color:var(--footer-text);line-height:60px}
</style>
</head>
<body>

<header class="site-header abs">
  <div class="brand abs">
    <span class="brand-mark"></span>
    <span class="brand-name">Copper Lantern</span>
  </div>
  <div class="search abs">
    <span>Search</span>
    <svg width="12" height="12" viewBox="0 0 12 12"><circle cx="5" cy="5" r="3.8" fill="none" stroke="#555" stroke-width="1.5"/><line x1="7.8" y1="7.8" x2="11" y2="11" stroke="#555" stroke-width="1.5"/></svg>
  </div>
  <nav class="main-nav abs">
    <span class="current">Home</span><span>Workouts</span><span>Book reviews</span><span>Blog</span><span>Coaching</span><span>About</span>
  </nav>
</header>

<section class="hero abs" role="img" aria-label="Sunset over a forested mountain lake">
  <svg class="hero-arrow abs" style="left:8px" viewBox="0 0 16 16"><path d="M11 3 L5 8 L11 13" fill="none" stroke="#fff" stroke-width="2"/></svg>
  <svg class="hero-arrow abs" style="right:8px" viewBox="0 0 16 16"><path d="M5 3 L11 8 L5 13" fill="none" stroke="#fff" stroke-width="2"/></svg>
  <div class="hero-caption abs">
    <h2>Aenean quis consequat velit, sed tincidunt ligula</h2>
    <div class="date">8 May, 2017</div>
    <p>Duis dignissim nisi eros, eget efficitur lorem interdum non. Sed quis mi a neque tempor suscipit. Vivamus sit amet ante nibh. Mauris ante turpis, condimentum at orci vel, ultrices luctus erat. Donec ornare porta sagittis, interdum et malesuada fames ac ante ipsum primis in faucibus.</p>
  </div>
</section>

<section class="welcome abs">
  <div class="welcome-media abs" role="img" aria-label="Video still of an athlete flipping a large tractor tyre in a gym">
    <svg class="play abs" viewBox="0 0 56 56"><circle cx="28" cy="28" r="28" fill="#fff"/><path d="M22 17 L39 28 L22 39 Z" fill="#111"/></svg>
  </div>
  <h1 class="abs">WELCOME</h1>
  <p class="abs">Phasellus nec pretium ex, at cursus tellus. Curabitur id arcu in ex pellentesque fermentum ut sit amet ipsum. Sed eu mi venenatis, fringilla risus eu, rhoncus tortor. Nunc sit amet nunc placerat, aliquet ante et, ultrices erat. Vivamus sed lectus et tellus tempus accumsan quis sed erat. Curabitur eu diam pulvinar, blandit magna vitae, venenatis sapien. Sed sollicitudin volutpat orci, ut iaculis dui ultrices vitae. Sed feugiat sagittis est aliquet euismod. Vestibulum diam turpis, blandit sit amet augue at, egestas imperdiet nisi. Vestibulum ante est, fringilla a arcu ac, porta cursus ipsum. Suspendisse sed risus mi. Aenean scelerisque quam ac dui tempus, ut porta ante pretium. Nunc eget eros neque.</p>
  <div class="btn-light abs">Read more</div>
  <div class="welcome-art abs" role="img" aria-label="Line-art mandala elephant decoration"></div>
</section>

<section class="featured abs" role="region" aria-label="Featured posts">
  <div class="abs" style="inset:0" role="img" aria-label="Dark forest background"></div>
  <h2 class="section-title abs" style="top:56px">FEATURED POSTS</h2>

  <article class="post-card abs" style="left:131px">
    <div class="post-media abs" style="background:linear-gradient(135deg,#5a7182,#2e3d47)" role="img" aria-label="Woman training with a cable machine"></div>
    <div class="post-date abs">8 MAY, 2017</div>
    <div class="post-body abs">
      <h3>Phasellus fringilla, ex eget malesuada finibus, felis felis pharetra felis</h3>
      <p>Mauris ante turpis, condimentum orci vel, ultrices luctus erat. Interdum et malesuada fames ac ante ipsum primis in faucibus. Nam massa orci, dictum vel turpis ut, gravida luctus ex. Nunc pretium accumsan est.</p>
    </div>
    <span class="post-more abs">MORE</span>
  </article>

  <article class="post-card abs" style="left:452px">
    <div class="post-media abs" style="background:linear-gradient(180deg,#a9c7da 0%,#d9d2c2 60%,#c9b896 100%)" role="img" aria-label="Man meditating on a beach"></div>
    <div class="post-date abs">8 MAY, 2017</div>
    <div class="post-body abs">
      <h3>Phasellus fringilla, ex eget malesuada finibus, felis felis pharetra felis</h3>
      <p>Mauris ante turpis, condimentum orci vel, ultrices luctus erat. Interdum et malesuada fames ac ante ipsum primis in faucibus. Nam massa orci, dictum vel turpis ut, gravida luctus ex. Nunc pretium accumsan est.</p>
    </div>
    <span class="post-more abs">MORE</span>
  </article>

  <article class="post-card abs" style="left:771px">
    <div class="post-media abs" style="background:linear-gradient(135deg,#8a6a4c,#c9a77e 50%,#6e5a45)" role="img" aria-label="Woman eating a healthy meal in a kitchen"></div>
    <div class="post-date abs">8 MAY, 2017</div>
    <div class="post-body abs">
      <h3>Phasellus fringilla, ex eget malesuada finibus, felis felis pharetra felis</h3>
      <p>Mauris ante turpis, condimentum orci vel, ultrices luctus erat. Interdum et malesuada fames ac ante ipsum primis in faucibus. Nam massa orci, dictum vel turpis ut, gravida luctus ex. Nunc pretium accumsan est.</p>
    </div>
    <span class="post-more abs">MORE</span>
  </article>

  <div class="btn-outline abs" style="top:516px">VIEW ALL</div>
</section>

<section class="workouts abs" role="region" aria-label="Workouts">
  <div class="abs" style="inset:0" role="img" aria-label="Tangled tree roots background"></div>
  <h2 class="section-title abs" style="top:73px">WORKOUTS</h2>

  <article class="workout abs" style="left:131px">
    <div class="workout-media" style="background:linear-gradient(180deg,#3a3a3a,#1c1c1c)" role="img" aria-label="Athlete balancing on a fitness ball"></div>
    <h3>Quisque urna lectus</h3>
    <p>Fusce rutrum mauris sed enim vestibulum, eu maximus justo posuere.</p>
  </article>
  <article class="workout abs" style="left:324px">
    <div class="workout-media" style="background:linear-gradient(180deg,#e6a43a,#c6661f 60%,#3a2414)" role="img" aria-label="Yoga pose silhouette at sunset"></div>
    <h3>Quisque urna lectus</h3>
    <p>Fusce rutrum mauris sed enim vestibulum, eu maximus justo posuere.</p>
  </article>
  <article class="workout abs" style="left:519px">
    <div class="workout-media" style="background:linear-gradient(180deg,#2a2a2a,#101010)" role="img" aria-label="Couple lifting barbells"></div>
    <h3>Quisque urna lectus</h3>
    <p>Fusce rutrum mauris sed enim vestibulum, eu maximus justo posuere.</p>
  </article>
  <article class="workout abs" style="left:713px">
    <div class="workout-media" style="background:linear-gradient(180deg,#c9d7b4,#7aa046 70%,#4d7a24)" role="img" aria-label="Man meditating on grass"></div>
    <h3>Quisque urna lectus</h3>
    <p>Fusce rutrum mauris sed enim vestibulum, eu maximus justo posuere.</p>
  </article>
  <article class="workout abs" style="left:906px">
    <div class="workout-media" style="background:linear-gradient(180deg,#3c3a3c,#1b1a1c)" role="img" aria-label="Dancer in a handstand pose"></div>
    <h3>Quisque urna lectus</h3>
    <p>Fusce rutrum mauris sed enim vestibulum, eu maximus justo posuere.</p>
  </article>

  <div class="btn-outline abs" style="top:435px">VIEW ALL</div>
</section>

<section class="newsletter abs">
  <div class="newsletter-title abs">
    <svg width="30" height="22" viewBox="0 0 30 22"><rect x="0" y="0" width="30" height="22" rx="2" fill="#fff"/><path d="M1 2 L15 13 L29 2" fill="none" stroke="#3f8b1d" stroke-width="2"/></svg>
    <span>Newsletter Subscribe</span>
  </div>
  <div class="field abs" style="left:508px">Full name</div>
  <div class="field abs" style="left:737px">Email Address</div>
  <div class="btn-dark abs">SUBSCRIBE</div>
</section>

<footer class="site-footer abs">
  <ul class="footer-links abs">
    <li>Home</li><li>Workouts</li><li>Book reviews</li><li>Blog</li><li>Coaching</li><li>About</li>
  </ul>
  <div class="footer-col blog-col abs">
    <h4>Blog</h4>
    <p>Aenean scelerisque quam ac dui tempus, ut porta ante pretium eget eros nequ</p>
    <p>Aenean scelerisque quam ac dui tempus, ut porta ante pretium eget eros nequ</p>
    <p>Aenean scelerisque quam ac dui tempus, ut porta ante pretium eget eros nequ</p>
  </div>
  <div class="footer-col coach-col abs">
    <h4>Coaching</h4>
    <ul>
      <li>• Sed bibendu</li><li>• Vestibulum ante</li><li>• Suspendisse tempus</li><li>• Etiam suscipit</li><li>• Nunc eget</li><li>• Phasellus</li>
    </ul>
  </div>
  <div class="footer-col about-col abs">
    <h4>About</h4>
    <p>Etiam suscipit lacus accumsan est rutrum dictum. Quisque aliquet porttitor luctus. Suspendisse sed risus mi. Aenean scelerisque quam ac dui tempus, ut porta ante pretium. Nunc eget eros neque. Phasellus nec ipsum mauris. Vivamus convallis velit in egestas convallis. Morbi molestie elementum sapien, quis porta enim.</p>
  </div>
  <span class="social abs" style="top:44px;background:#3b5a9a"></span>
  <span class="social abs" style="top:89px;background:#2aa3df"></span>
  <span class="social abs" style="top:134px;background:#d8452e"></span>
  <span class="social abs" style="top:179px;background:#c9202a"></span>
</footer>

<div class="copyright abs">Copyright © 2017 Copper Lantern. All rights reserved.</div>

</body>
</html>
```